Design a Facebook landing page for Plume Eatery Guide Facebook page

Hi Freelancers,
This is an inquiry a contest to create a landing page for my Facebook page.
I am open to all ideas, you can look into my Facebook and website page to have a clearer idea of my services.

https://www.facebook.com/plumeeateryguide
http://www.plumeeateryguide-example.com

```html
<!DOCTYPE html>
<html lang="en">
<head>
<meta charset="utf-8">
<title>Plume Eatery Guide – Facebook Cover</title>
<link rel="stylesheet" href="https://fonts.googleapis.com/css2?family=Arimo:wght@400;700&display=swap">
<style>
  :root {
    --yellow: #f7c300;
    --black: #000000;
    --ink: #1a1a1a;
    --white: #ffffff;
    --rule: #b9b9b9;
    --scene-light: #eeeae4;
    --scene-dark: #8a7f73;
    --waiter-light: #d9d4cc;
    --waiter-dark: #2b2623;
  }
  html, body {
    margin: 0;
    padding: 0;
    overflow: hidden;
    background: var(--white);
  }
  .cover {
    position: relative;
    width: 1200px;
    height: 444px;
    overflow: hidden;
    background: var(--white);
    font-family: "Arimo", Arial, sans-serif;
    color: var(--ink);
  }
  .dining-scene {
    position: absolute;
    left: 0; top: 120px;
    width: 370px; height: 324px;
    background: linear-gradient(160deg, var(--scene-light) 0%, #d8cfc3 55%, var(--scene-dark) 100%);
  }
  .corner-band {
    position: absolute;
    left: 0; top: 0;
    width: 780px; height: 200px;
  }
  .bartender {
    position: absolute;
    left: 330px; top: 78px;
    width: 225px; height: 366px;
    background: linear-gradient(180deg, var(--waiter-light) 0%, #6b625b 45%, var(--waiter-dark) 100%);
    border-radius: 90px 90px 0 0;
  }
  .cta {
    position: absolute;
    display: flex;
    align-items: center;
    justify-content: center;
    background: var(--black);
    color: var(--white);
    font-weight: 700;
    font-size: 27px;
  }
  .cta--subscribe { left: 70px; top: 17px; width: 201px; height: 40px; }
  .cta--post { left: 152px; top: 78px; width: 187px; height: 40px; }
  .cta-note {
    position: absolute;
    left: 281px; top: 27px;
    font-size: 21px;
    color: var(--black);
  }
  .reasons-title {
    position: absolute;
    left: 800px; top: 24px;
    width: 400px;
    text-align: center;
    margin: 0;
    font-size: 33px;
    font-weight: 700;
    color: var(--black);
  }
  .reasons {
    position: absolute;
    left: 656px; top: 82px;
    margin: 0; padding: 0;
    list-style: none;
  }
  .reason {
    position: relative;
    height: 52px;
    margin-bottom: 17px;
    display: flex;
    align-items: center;
  }
  .reason-bar {
    position: absolute;
    left: 34px; top: 0;
    width: 452px; height: 52px;
    background: var(--black);
  }
  .reason-num {
    position: relative;
    z-index: 1;
    width: 40px; height: 40px;
    border-radius: 50%;
    background: var(--yellow);
    box-shadow: 0 0 0 5px var(--white), 0 0 0 7px var(--yellow);
    color: var(--white);
    font-weight: 700;
    font-size: 22px;
    display: flex;
    align-items: center;
    justify-content: center;
    margin-left: 6px;
  }
  .reason-text {
    position: relative;
    z-index: 1;
    margin-left: 22px;
    color: var(--white);
    font-size: 15.5px;
  }
  .brand {
    position: absolute;
    left: 585px; top: 370px;
    width: 600px;
    display: flex;
    align-items: center;
    gap: 14px;
  }
  .brand-rule {
    flex: 1;
    border-top: 2px dotted var(--rule);
  }
  .brand-name {
    font-size: 50px;
    font-weight: 700;
    color: var(--ink);
    white-space: nowrap;
  }
</style>
</head>
<body>
  <main class="cover">
    <div class="dining-scene" role="img" aria-label="Photo of an elegant restaurant dining room with laid tables and staff setting them"></div>

    <svg class="corner-band" viewBox="0 0 780 200" aria-hidden="true">
      <polygon points="0,0 770,0 150,192 0,108" fill="var(--yellow)"/>
      <polygon points="770,0 150,192 205,192" fill="var(--black)"/>
    </svg>

    <div class="bartender" role="img" aria-label="Photo of a waiter in a black vest pouring a cocktail from a shaker"></div>

    <div class="cta cta--subscribe">Subscribe</div>
    <span class="cta-note">to our weekly email</span>
    <div class="cta cta--post">Post a job</div>

    <h2 class="reasons-title">Why choose us?</h2>
    <ol class="reasons">
      <li class="reason"><span class="reason-bar"></span><span class="reason-num">1</span><span class="reason-text">Free weekly email of restaurant job openings.</span></li>
      <li class="reason"><span class="reason-bar"></span><span class="reason-num">2</span><span class="reason-text">Subscribers to get weekly emails on Monday.</span></li>
      <li class="reason"><span class="reason-bar"></span><span class="reason-num">3</span><span class="reason-text">Job posting available till 10 P.M on Sunday.</span></li>
      <li class="reason"><span class="reason-bar"></span><span class="reason-num">4</span><span class="reason-text">Proud supporters to fight hunger in our communities.</span></li>
    </ol>

    <div class="brand">
      <span class="brand-rule"></span>
      <span class="brand-name">Plume Eatery Guide</span>
      <span class="brand-rule"></span>
    </div>
  </main>
</body>
</html>
```